Real Estate Business Cards

Looking for a clean, sharp and professional look for our Real Estate investment Fund that invests in Multi Family Apartment buildings.

Target Market(s)

Real Estate Fund

Industry/Entity Type

Real Estate

Contact Information for Business Card

Company Description: Real Estate Investment Fund
Company Name: RKW Holdings
Name: Marcus Olvane
Cell: (917) 482-0657
Email: marcus@rkwholdings-example.com
Website: www.rkwholdings-example.com
Address: 418, 9th Street, Brooklyn NY 11218

Colors

Designer to choose colors to be used in the design.

Requirements
Nice to have
• Colors to match logo

```html
<!DOCTYPE html>
<html lang="en">
<head>
<meta charset="utf-8">
<title>RKW Holdings – Business Cards</title>
<link rel="stylesheet" href="https://fonts.googleapis.com/css2?family=Jost:wght@400&family=Crimson+Pro:wght@400;600&display=swap">
<style>
  :root {
    --page: #ffffff;
    --stage: #f1f1f1;
    --card: #222222;
    --shadow: #0b0b0b;
    --brand-blue: #0e74a8;
    --name-grey: #5a5a5a;
    --detail-grey: #474747;
    --band-text: #151515;
  }
  * { margin: 0; padding: 0; box-sizing: border-box; }
  html, body {
    width: 1200px; height: 980px; overflow: hidden;
    background: var(--page);
  }
  .canvas { position: relative; width: 1200px; height: 980px; }
  .stage {
    position: absolute; left: 45px; top: 40px;
    width: 1098px; height: 892px;
    background: var(--stage);
  }
  .card-shadow {
    position: absolute;
    background: var(--shadow);
    filter: blur(6px);
  }
  .card {
    position: absolute; left: 355px; width: 515px;
    background: var(--card);
    overflow: hidden;
  }
  .card--front { top: 165px; height: 315px; }
  .card--back  { top: 538px; height: 310px; }
  .shadow--front { left: 333px; top: 198px; width: 515px; height: 292px; }
  .shadow--back  { left: 333px; top: 570px; width: 515px; height: 290px; }

  .brand-name {
    position: absolute; left: 0; right: 0;
    text-align: center;
    font-family: "Crimson Pro", Georgia, serif;
    font-weight: 400;
    color: var(--brand-blue);
    white-space: nowrap;
  }
  .card--front .brand-name { top: 82px; font-size: 30px; }
  .card--back .brand-name { top: 196px; font-size: 44px; }

  .brand-square {
    position: absolute; left: 239px; top: 92px;
    width: 37px; height: 37px;
    border: 3px solid var(--brand-blue);
  }

  .person-name {
    position: absolute; left: 0; right: 0; top: 163px;
    text-align: center;
    font-family: "Jost", Arial, sans-serif;
    font-size: 26px; color: var(--name-grey);
  }
  .name-rule {
    position: absolute; left: 128px; top: 197px;
    width: 255px; height: 2px; background: var(--brand-blue);
  }
  .contact {
    position: absolute; left: 0; right: 0;
    text-align: center;
    font-family: "Crimson Pro", Georgia, serif;
    font-size: 13px; letter-spacing: 1px;
    color: var(--detail-grey);
    white-space: nowrap;
  }
  .contact--line1 { top: 221px; word-spacing: 2px; }
  .contact--line1 .gap { display: inline-block; width: 18px; }
  .contact--line2 { top: 239px; }

  .web-band {
    position: absolute; left: 0; bottom: 0;
    width: 100%; height: 30px;
    background: var(--brand-blue);
    display: flex; align-items: center; justify-content: center;
    font-family: "Crimson Pro", Georgia, serif;
    font-weight: 600; font-size: 12px;
    letter-spacing: 3px; color: var(--band-text);
  }
</style>
</head>
<body>
<div class="canvas">
  <div class="stage"></div>

  <div class="card-shadow shadow--front"></div>
  <section class="card card--front">
    <div class="brand-name">RKW Holdings</div>
    <div class="person-name">Marcus Olvane</div>
    <div class="name-rule"></div>
    <p class="contact contact--line1">Phone: (917) 482-0657<span class="gap"></span>Email: marcus@rkwholdings-example.com</p>
    <p class="contact contact--line2">Address : 418, 9th Street, Brooklyn NY 11218</p>
    <div class="web-band">www.rkwholdings-example.com</div>
  </section>

  <div class="card-shadow shadow--back"></div>
  <section class="card card--back">
    <div class="brand-square"></div>
    <div class="brand-name">RKW Holdings</div>
  </section>
</div>
</body>
</html>
```